price list for web and print- sending to inquiring clients and use as promo material

Hello
I need a graphic design for my photography price list/s. I am a people photographer. The first of 6 price sheets will be for head shots- I would like a price sheet that captures the prospective clients' attention. The info and visual should be compelling and easy to digest. It should be simple yet interesting. I will provide you with some pictures but you do not have to include them. I have a studio indoors and outdoors also working on location. This design should be for email and print. The picture of "ingrid" is me and I use that on all my profiles. I like the fonts in the logo but it is too boxy and rigid

Target Market(s)

repeat client, word of mouth referrals, new people but aquaintances of others that might know me

Industry/Entity Type

Graphic Design

Font styles to use
Serif
Sans Serif
Script

Requirements
Must have
• prices and maybe some words about my services that I sent in... Please tie it together as best as possible..
Nice to have
• Loosen up my logo.. it is in a box.....contemporary design but not something that would not fit in with corporate.. I like this headline
• "Create a great first impression with your professional headshots"
• I sent in other copy and my logo(sent in the picture drop box)

```html
<!DOCTYPE html>
<html lang="en">
<head>
<meta charset="utf-8">
<title>Ingrid M. Hale Photography – Headshot Price Sheet</title>
<link rel="stylesheet" href="https://fonts.googleapis.com/css2?family=Nunito+Sans:ital,wght@0,300;0,400;0,600;0,700;0,800;1,300&display=swap">
<style>
  :root {
    --ink: #000000;
    --paper: #ffffff;
    --brown: #8a5a2c;
    --card: #f8f0ea;
    --body-font: "Nunito Sans", "Avenir Next", Arial, sans-serif;
  }
  * { box-sizing: border-box; margin: 0; padding: 0; }
  html, body { width: 900px; height: 1200px; overflow: hidden; background: var(--paper); }
  body { font-family: var(--body-font); color: var(--brown); }
  .sheet { position: relative; width: 900px; height: 1200px; overflow: hidden; }

  .brand {
    position: absolute; top: 36px; left: 0; width: 900px;
    text-align: center; font-size: 22px; font-weight: 700; color: var(--ink);
    letter-spacing: 0.5px;
  }

  .headline {
    position: absolute; top: 147px; left: 0; width: 900px; text-align: center;
    font-size: 24px; font-weight: 800; color: var(--ink);
  }
  .headline em { font-style: normal; color: var(--brown); }

  .feature { position: absolute; top: 246px; width: 248px; }
  .feature-label {
    display: block; width: 122px; height: 19px; margin-left: 62px;
    background: var(--ink); color: var(--paper); border-radius: 3px;
    font-size: 15px; font-weight: 700; text-align: center; line-height: 19px;
  }
  .feature-label.wide { width: 173px; margin-left: 36px; }
  .feature p { font-size: 16px; font-weight: 300; line-height: 19.5px; margin-top: 4px; }
  .feature-experience { left: 61px; }
  .feature-turnaround { left: 327px; }
  .feature-enjoyable { left: 593px; }

  .price-title {
    position: absolute; top: 426px; left: 0; width: 900px; text-align: center;
    font-size: 19px; font-weight: 700; color: var(--ink);
  }

  .package {
    position: absolute; width: 244px; background: var(--card);
    border-radius: 8px; padding: 4px 8px 10px;
    font-size: 16px; font-weight: 300; line-height: 19.5px;
  }
  .package h3 { font-size: 19px; font-weight: 600; color: var(--ink); line-height: 25px; }
  .package .tagline { font-style: italic; }
  .package .price { font-size: 19px; font-weight: 800; color: var(--ink); margin-top: 19px; line-height: 22px; }
  .package .extra strong { font-weight: 700; }
  .package-entry { left: 168px; top: 472px; height: 200px; }
  .package-two { left: 487px; top: 472px; height: 235px; }
  .package-premium { left: 168px; top: 726px; height: 233px; }
  .package-location { left: 487px; top: 726px; height: 158px; }

  .group-rates {
    position: absolute; left: 67px; top: 1015px; color: var(--ink);
    font-size: 15px; font-weight: 300; line-height: 19px;
  }
  .group-rates p + p { margin-top: 19px; }
  .group-rates strong { font-weight: 700; }

  .footer-band { position: absolute; left: 0; bottom: 0; width: 900px; height: 20px; background: var(--ink); }
</style>
</head>
<body>
<div class="sheet">
  <div class="brand">Ingrid M. Hale Photography</div>

  <h1 class="headline">Create a great first impression with your <em>professional</em> headshots</h1>

  <section class="feature feature-experience">
    <span class="feature-label">Experience</span>
    <p>Ingrid is an accomlished profes-<br>sional photographer who has<br>helped thousands of clients.She<br>is an expert&nbsp; at helping you look<br>confident and approachable.</p>
  </section>
  <section class="feature feature-turnaround">
    <span class="feature-label wide">24 Hour Turnaround</span>
    <p>Your time is valuable.Ingrid can<br>complete the photoshoot in just<br>30 minutes .(Or as long as you<br>want.) Our process is designed to<br>save you time.</p>
  </section>
  <section class="feature feature-enjoyable">
    <span class="feature-label">Enjoyable</span>
    <p>You can look forward to an enjoy-<br>able photo session wit Ingrid’s<br>professional guidance.Ingrid<br>helps make the experince fun.</p>
  </section>

  <h2 class="price-title">Price Sheet</h2>

  <article class="package package-entry">
    <h3>Entry Package</h3>
    <div class="tagline">Quick and Simple</div>
    <div>One pose</div>
    <div>One wardrobe</div>
    <div>One selected image retouched</div>
    <div class="price">$175</div>
    <div class="extra">Additional images just <strong>$75</strong><br>each</div>
  </article>

  <article class="package package-two">
    <h3>2 Pose Package</h3>
    <div class="tagline">Most Popular</div>
    <div>Two pose</div>
    <div>Two wardrobe</div>
    <div>Two selected image retouched</div>
    <div>One or two background<br>changes</div>
    <div class="price">$175</div>
    <div class="extra">Additional images just <strong>$75</strong><br>each</div>
  </article>

  <article class="package package-premium">
    <h3>Premium Package</h3>
    <div class="tagline">Get it all</div>
    <div>Four pose</div>
    <div>3-4 wardrobe</div>
    <div>4 selected image retouched</div>
    <div>2-3 background changes</div>
    <div>Optional outdoor studio</div>
    <div class="price">$525</div>
    <div class="extra">Additional images just <strong>$75</strong><br>each</div>
  </article>

  <article class="package package-location">
    <h3>At your location</h3>
    <div>Minimum of 5 people</div>
    <div>One selected image retouched</div>
    <div class="price">$250</div>
    <div class="extra">Additional images just <strong>$50</strong><br>each</div>
  </article>

  <section class="group-rates">
    <p>If possible, we like 1⁄2 hour appts for each person so they can view their images on the computer</p>
    <p>5-10 people <strong>$150</strong> EACH<br>11-20 people <strong>$100</strong> each<br>20+ <strong>$75</strong> each</p>
  </section>

  <div class="footer-band"></div>
</div>
</body>
</html>
```